Brochure Design Project

We are looking for a brochure to communicate the various different program we offer within the "Trailside & Habitat Studies" department
( www.fernpath.kx29.example.ca )
We have a large photo bank of students engaged in our programs and can willingly provide them if requested.

Target Market(s)

parents, students, academics, administrators

Industry/Entity Type

Bank

Requirements
Must have
• nature based theme. adventure and ecology.

```html
<!DOCTYPE html>
<html lang="en">
<head>
<meta charset="utf-8">
<title>Trailside &amp; Habitat Studies Brochure</title>
<link href="https://fonts.googleapis.com/css2?family=Oswald:wght@600&family=Roboto+Condensed:ital,wght@0,400;0,700;1,400&family=Libre+Baskerville:wght@700&display=swap" rel="stylesheet">
<style>
:root{
  --page:#e9e4da;
  --cream:#f8f1d8;
  --taupe:#8d7a68;
  --taupe-dark:#6f5e4f;
  --orange:#ea7a2b;
  --orange-deep:#d2601a;
  --ink:#2d2620;
  --brown:#5a2a14;
  --link:#e0702a;
  --white:#ffffff;
}
*{margin:0;padding:0;box-sizing:border-box}
html,body{width:1200px;height:1000px;overflow:hidden;background:var(--page)}
.brochure{position:absolute;left:40px;top:40px;width:1120px;height:920px;background:var(--cream);display:flex;box-shadow:0 4px 14px rgba(0,0,0,.18);overflow:hidden}
.panel{position:relative;width:373px;height:100%}
.panel--left,.panel--middle{background:var(--taupe)}
.panel--right{background:var(--cream);width:374px}
.card{position:absolute;background:var(--cream);border-radius:26px}
.panel--left .card{left:26px;top:60px;width:330px;height:790px}
.panel--middle .card{left:16px;top:20px;width:340px;height:660px}
.tab{position:absolute;z-index:3;background:var(--orange);color:var(--white);font:600 23px/1.05 "Oswald",sans-serif;padding:10px 16px;box-shadow:0 2px 0 var(--orange-deep)}
.panel--left .tab{left:14px;top:40px;width:240px}
.panel--middle .tab{left:6px;top:14px;width:250px}
.panel--right .tab{left:0;top:0;width:374px;padding:14px 16px}
.body{position:absolute;z-index:2;font:400 13px/1.3 "Roboto Condensed",sans-serif;color:var(--ink)}
.panel--left .body{left:42px;top:108px;width:302px}
.panel--middle .body{left:32px;top:96px;width:314px}
.panel--right .body{left:26px;top:92px;width:328px}
.tips{list-style:none}
.tips li::before{content:"·";margin-right:8px}
.link{color:var(--link)}
.cite{display:block;color:var(--link);font-style:italic;margin-top:10px;padding-left:14px}
.photo{position:absolute}
.photo--kayaks{left:0;bottom:0;width:373px;height:100px;background:linear-gradient(180deg,#4d6a5c 0%,#7f9c9a 55%,#c9d7d8 100%);clip-path:polygon(0 25%,30% 12%,60% 18%,100% 0,100% 100%,0 100%)}
.photo--run{left:0;top:665px;width:373px;height:255px;background:linear-gradient(160deg,#2f5b1f 0%,#6f9b3a 50%,#9bbf56 100%)}
.logo-strip{position:absolute;left:70px;bottom:0;width:303px;height:110px;background:var(--white);border-radius:160px 0 0 0;display:flex;align-items:center;justify-content:space-around;padding:18px 10px 0 30px}
.partner{display:flex;align-items:center;gap:5px;font:400 12px/1 "Roboto Condensed",sans-serif;color:var(--ink)}
.partner i{width:14px;height:14px;border-radius:50%;background:var(--taupe)}
.frame{position:absolute;left:42px;top:640px;width:230px;height:170px;background:var(--white);padding:8px;box-shadow:0 0 0 4px var(--orange)}
.photo--trail{width:100%;height:100%;background:linear-gradient(180deg,#6e8f3c 0%,#3d6a2a 55%,#b2a998 100%)}
.photo--rock{right:0;top:610px;width:150px;height:240px;background:radial-gradient(circle at 60% 40%,#e9763a 0%,#cf5a27 45%,#a6826b 100%);border-radius:60px 0 0 60px}
.fold{position:absolute;left:0;top:70px;width:14px;height:850px;background:linear-gradient(90deg,var(--orange-deep),#f0b43a)}
.footer{position:absolute;left:0;bottom:0;width:374px;height:80px;background:var(--cream);padding:12px 16px 0 92px}
.footer__mark{position:absolute;left:22px;bottom:8px;width:44px;height:58px;background:var(--brown)}
.footer__district{font:700 13px/1.1 "Roboto Condensed",sans-serif;color:var(--brown)}
.footer__name{font:700 16px/1.15 "Libre Baskerville",serif;color:var(--brown)}
.footer__contact{display:flex;justify-content:space-between;font:400 12px/1.3 "Roboto Condensed",sans-serif;color:var(--taupe-dark)}
</style>
</head>
<body>
<main class="brochure">

  <section class="panel panel--left">
    <div class="card"></div>
    <h2 class="tab">Ways to Get Outside!</h2>
    <div class="body">
      <p>With over 80% of Canadians living in urban areas, our feet are more familiar with concrete than they are with the forest floor. Canadians spend over 90% of their time indoors and on average, six or more hours a day in front of a screen. This disconnection from the natural world is called Nature Deficit Disorder and is correlated with the increased incidence of obesity, heart disease, asthma, depression, and stress. Fortunately, the anecdote to this modern-day ailment is just beyond our front doors. Take time every day to take your vitamin O(utside)! Here is how:</p>
      <ul class="tips">
        <li>Explore the wild places in your neighborhood.</li>
        <li>Rediscover and reclaim your childhood wild places with your children.</li>
        <li>Commit to sitting still in nature daily for a minimum of 20 minutes, and then share this experience with others by telling them about your solo time.</li>
        <li>Find a local group that engages its members in outdoor recreation; meet new friends to get outdoors with!</li>
        <li>Discover the names and uses of local flora and fauna in your region by investing in a plant or animal guidebook. You'll be guiding interpretive walks in no time!</li>
        <li>Get dirty, play in the mud, and jump in puddles!</li>
        <li>Use nature as inspiration to create art, or better yet make natural art installments outside – think Elsie Varga!</li>
        <li>Create a garden, and enjoy the plethora of fruits born of this labor.</li>
      </ul>
    </div>
    <div class="photo photo--kayaks" role="img" aria-label="Photo of students cheering in canoes on a lake"></div>
  </section>

  <section class="panel panel--middle">
    <div class="card"></div>
    <h2 class="tab">Why is it important to spend time outdoors?</h2>
    <div class="body">
      <p>Well, here is what the research says!</p>
      <p>Regular contact with nature promotes healthier social behavior and lessens social dysfunction, helps alleviate stress, improves resilience, promotes optimal psychological functioning, improves recovery from physical trauma, and reduces mortality.</p>
      <p>A child's time in nature provides the benefits of creating sacred places, development of self and greater independence.</p>
      <p>Children with ADHD who regularly play in green settings have milder symptoms than children who play in built outdoor and indoor settings.</p>
      <p>School gardens positively impact children's learning and behavior.</p>
      <p>Pregnant women living in areas with more trees had better birth outcomes.</p>
      <p>Outdoor experience for teens has self-reported life-changing results.</p>
      <p>Children's emotional affinity towards nature is a strong predictor of their willingness to protect the environment.</p>
      <p>All research summarized &amp; provided by the Kids Outside Alliance</p>
      <p class="link">http://www.kidsoutside.example.org/</p>
    </div>
    <div class="photo photo--run" role="img" aria-label="Photo of students running across a grassy field"></div>
    <div class="logo-strip">
      <span class="partner"><i></i>Green Toolkit</span>
      <span class="partner"><i></i>Ridgeline Academy</span>
      <span class="partner"><i></i>STRIDE</span>
    </div>
  </section>

  <section class="panel panel--right">
    <div class="fold"></div>
    <h2 class="tab">Trailside &amp; Habitat Studies Department (SD29)</h2>
    <div class="body">
      <p>The Trailside &amp; Habitat Studies Department is dedicated to providing students with educational opportunities that reinforce their connection to the natural world and foster sustainability. We focus on giving students the necessary skills to think critically about personal choices and the relationships between society, economy, culture and the environment. Through action leadership, skill development and inspired experience, our students are empowered to make positive change in their communities. We offer numerous programs and have highlighted a few in this document.</p>
      <p>"The Trailside &amp; Habitat Studies Programs in School District 29 help to fill a huge void in modern society: the void between what's taught in the classroom and the day-to-day miracles happening outside. I can think of no better way to close this gap than to get kids into wild areas where Nature does the teaching, affecting students in ways that stick with them for the rest of their lives."</p>
      <span class="cite">- Marlow Tennant, Explorer, Wildlife Biologist, Author</span>
    </div>
    <div class="photo photo--rock" role="img" aria-label="Close-up photo of orange lichen on a rock"></div>
    <div class="frame"><div class="photo--trail" role="img" aria-label="Photo of a group of students hiking down a forest trail"></div></div>
    <footer class="footer">
      <div class="footer__mark"></div>
      <div class="footer__district">School District 29</div>
      <div class="footer__name">Trailside &amp; Habitat Studies</div>
      <div class="footer__contact"><span>www.fernpath.kx29.example.ca</span><span>604 555-0147</span></div>
    </footer>
  </section>

</main>
</body>
</html>
```